Condo Debts Collection Business needs a Web Design (Contest)

I need a site for a client, who works with condo debts collection, and ensure all revenues provided by condo fees will be always available to the building manager of condo on a specific date, regardless of defaults.I have the logo of the companies, and some requirements on layout (kind of slider, menu options, phone number on a noble position, etc).
Updates

Designs look the same

Target Market(s)

I have two targets for this design: - Condominium's building manager. This target is looking for a solution to overdue debts on it's condo. - Residents on condominiums. This target wants to live in a better place, where their neighbors pay their condominium fees on time.

Number of Pages Required

1 page

Requirements
Must have
• - Slider with title, some short text related, a nice image (I prefer happy and/or peaceful family, people doing business, happy friends, and so on).
• - I have a special attention to menu. I'm looking for one I can have a nice effect, more elegant, charming, kind of innovative.
• - Phone number on the top (or clearly visible).
• - Member log in area or icon on the top (or clearly visible).
• - News/articles area.
• - Modern fonts, with good quality, sans-serif on areas where reading is more intensive (prefer Google web-fonts).
• - Colors specified on attached files.
• - Header similar or inspired by the "FILE 3"
Nice to have
• - Clear background color, cause it's better to read larger texts (like articles). Dark backgrounds makes reading difficult.
• - A site with effects (like shadows, lines, gradients, lights) is usually pretty.
• - I pay attention on beautiful footers.
Should not have
• - Images with a lot of money (I don't sell richness, I sell tranquility, peace, harmony, safety).
• - Poor menu.
• - Lots of curves. My customer asked for straight lines.

```html
<!DOCTYPE html>
<html lang="en">
<head>
<meta charset="utf-8">
<title>Serena Condo — Condo Fee Guarantee</title>
<link href="https://fonts.googleapis.com/css2?family=Montserrat:wght@400;500;600;700&display=swap" rel="stylesheet">
<style>
  :root{
    --orange:#e57a1a;
    --navy:#0b2d5b;
    --navy-deep:#0a2a55;
    --blue:#0653a3;
    --blue-mid:#0a4a8f;
    --text-blue:#0d3a78;
    --field:#cfd8e3;
    --white:#ffffff;
  }
  *{margin:0;padding:0;box-sizing:border-box}
  html,body{width:1200px;height:1200px;overflow:hidden;background:var(--white)}
  body{font-family:'Montserrat',sans-serif;position:relative;color:var(--text-blue)}
  .abs{position:absolute}
  .btn{position:absolute;display:flex;align-items:center;justify-content:center;background:var(--orange);color:var(--white);font-weight:700;font-size:11px;letter-spacing:2.6px;text-transform:uppercase}

  /* hero */
  .hero{left:0;top:0;width:1200px;height:128px;background:var(--orange);overflow:hidden}
  .hero-photo{position:absolute;left:372px;top:0;width:828px;height:128px;
    background:linear-gradient(100deg,#6a4a3a 0%,#a47862 25%,#e9e3dd 45%,#cfc9c4 70%,#5c5750 100%);
    clip-path:polygon(26px 0,100% 0,100% 100%,0 100%)}
  .hero-cta{left:95px;top:0;width:168px;height:36px;background:var(--navy);color:var(--white);font-size:11px;font-weight:700;letter-spacing:2.6px;display:flex;align-items:center;justify-content:center}
  .phone-box{left:824px;top:64px;width:376px;height:64px;background:var(--navy);clip-path:polygon(12px 0,100% 0,100% 100%,0 100%);display:flex;align-items:center;padding-left:52px;gap:10px;color:var(--white);font-weight:700;font-size:22px}

  .intro{left:140px;top:176px;width:920px;text-align:center;font-size:16px;font-weight:700;line-height:24px;color:var(--text-blue)}
  .divider-glow{left:140px;top:260px;width:1040px;height:14px;background:radial-gradient(ellipse at 50% 0,rgba(11,45,91,.13),rgba(11,45,91,0) 70%)}

  /* about */
  .about-text{left:96px;top:332px;width:510px;font-size:14px;line-height:21.6px;color:var(--text-blue)}
  .about-text p+p{margin-top:22px}
  .building{left:596px;top:320px;width:604px;height:368px;
    background:linear-gradient(90deg,#6b3a22 0%,#8a4f2e 35%,#e6e8f2 55%,#dfe3ef 70%,#7a4528 85%,#5e3420 100%);
    clip-path:polygon(140px 6px,100% 0,100% 100%,0 100%)}

  /* news */
  .news{left:0;top:688px;width:1200px;height:336px;background:linear-gradient(180deg,var(--blue) 0%,var(--blue-mid) 60%,#0b3f7a 100%)}
  .news-title{position:absolute;left:0;width:1200px;top:50px;text-align:center;color:var(--white);font-weight:700;font-size:21px}
  .article{position:absolute;top:108px;width:310px;color:var(--white)}
  .article time{display:block;font-size:11px;font-weight:500}
  .article h3{margin-top:6px;color:var(--orange);font-size:13px;font-weight:700;letter-spacing:2.6px}
  .article p{margin-top:8px;font-size:14px;line-height:21.6px}
  .article .btn{position:relative;margin-top:14px;width:128px;height:32px}
  .col-rule{position:absolute;top:109px;width:1px;height:166px;background:rgba(255,255,255,.25)}

  /* footer */
  .footer{left:0;top:1024px;width:1200px;height:136px;background:var(--navy-deep)}
  .footer-shade{position:absolute;left:0;top:0;width:528px;height:136px;background:#0c3263;clip-path:polygon(0 0,100% 0,96% 100%,0 100%)}
  .social{position:absolute;left:51px;width:9px;height:9px;background:var(--white)}
  .foot-rule{position:absolute;left:84px;top:32px;width:1px;height:72px;background:rgba(255,255,255,.3)}
  .contact{position:absolute;left:107px;top:39px;width:400px;font-size:10px;line-height:15px;color:var(--white)}
  .contact .mail{color:var(--orange);font-weight:700}
  .newsletter-title{position:absolute;left:592px;top:40px;color:var(--white);font-size:13px;font-weight:700;letter-spacing:2.6px}
  .field{position:absolute;top:66px;height:32px;width:224px;background:var(--field);color:var(--text-blue);font-size:12px;font-weight:700;display:flex;align-items:center;padding-left:14px}

  .bar{left:0;top:1160px;width:1200px;height:40px;background:var(--orange);display:flex;align-items:center;justify-content:space-between;padding:0 48px}
  .copyright{font-size:9px;color:var(--navy)}
  .menu{display:flex;gap:28px;list-style:none}
  .menu li{color:var(--white);font-size:9px;font-weight:700;letter-spacing:2px}
</style>
</head>
<body>

<header class="abs hero">
  <div class="hero-photo" role="img" aria-label="Photo of a smiling mother and child sharing a happy moment at home"></div>
  <div class="abs hero-cta">FIND OUT MORE</div>
  <div class="abs phone-box">
    <svg width="26" height="26" viewBox="0 0 26 26" aria-hidden="true">
      <circle cx="13" cy="13" r="13" fill="#e57a1a"/>
      <path d="M8 6.5l3 3-1.6 2.2a9 9 0 0 0 4.9 4.9l2.2-1.6 3 3-1.8 2.2C11 19.5 6.5 15 5.8 8.3z" fill="#0b2d5b"/>
    </svg>
    <span>4120-5510 / 4120-5520</span>
  </div>
</header>

<p class="abs intro">Lorem ipsum dolor sit amet, consectetur adipiscing elit, sed do eiusmod tempor incididunt ut labore et dolore magna aliqua. Ut enim ad minim veniam, quis nostrud exercitatio</p>
<div class="abs divider-glow"></div>

<section>
  <div class="abs about-text">
    <p>Lorem ipsum dolor sit amet, consectetur adipiscing elit, sed do eiusmod tempor incididunt ut labore et dolore magna aliqua. Ut enim ad minim veniam, quis nostrud exercitation ullamco laboris nisi ut aliquip ex ea commodo consequat. Duis aute irure dolor in reprehenderit in voluptate velit esse cillum dolore eu fugiat nulla pariatur.</p>
    <p>Sed ut perspiciatis unde omnis iste natus error sit voluptatem accusantium doloremque laudantium, totam rem aperiam, eaque ipsa quae ab illo inventore veritatis et quasi architecto beatae vitae dicta sunt explicabo.</p>
  </div>
  <div class="btn" style="left:96px;top:565px;width:256px;height:40px">I AM A BUILDING MANAGER</div>
  <div class="btn" style="left:384px;top:565px;width:184px;height:40px">I AM A RESIDENT</div>
  <div class="abs building" role="img" aria-label="Photo of a modern residential building with wooden slatted balconies against a pale sky"></div>
</section>

<section class="abs news">
  <h2 class="news-title">Latest News</h2>
  <article class="article" style="left:96px">
    <time>23 March 2019</time>
    <h3>NEWS ARTICLE TITLE</h3>
    <p>Quis nostrud exercitation ullamco laboris nisi ut aliquip ex ea commodo consequat. Duis aute irure dolor in reprehenderit ...</p>
    <div class="btn">READ MORE</div>
  </article>
  <div class="col-rule" style="left:424px"></div>
  <article class="article" style="left:453px">
    <time>23 March 2019</time>
    <h3>NEWS ARTICLE TITLE</h3>
    <p>Duis aute irure dolor reprehenderit voluptate velit esse cillum dolore eu fugiat nulla pariatu excepteur sint occaecat cupidatat ...</p>
    <div class="btn">READ MORE</div>
  </article>
  <div class="col-rule" style="left:776px"></div>
  <article class="article" style="left:806px">
    <time>23 March 2019</time>
    <h3>NEWS ARTICLE TITLE</h3>
    <p>Excepteur sint occaecat cupidatat proident, sunt in culpa qui officia deserunt mollit anim id est laborum unde omnis iste natus ...</p>
    <div class="btn">READ MORE</div>
  </article>
</section>

<footer class="abs footer">
  <div class="footer-shade"></div>
  <span class="social" style="top:41px" aria-label="Social link"></span>
  <span class="social" style="top:65px" aria-label="Social link"></span>
  <span class="social" style="top:89px" aria-label="Social link"></span>
  <div class="foot-rule"></div>
  <div class="contact">
    <div>Rua das Acácias, 418, Edifício Horizonte, sala 702 - Jardim Sul - Palhoça - SC CEP.88 132-450</div>
    <div style="margin-top:5px">4120-5510 / 4120-5520</div>
    <div class="mail" style="margin-top:3px">contato@serenacondo.com.br</div>
  </div>
  <div class="newsletter-title">SIGN UP TO OUR NEWSLETTER</div>
  <div class="field" style="left:592px">Name</div>
  <div class="field" style="left:832px">Email Address</div>
  <div class="btn" style="left:1072px;top:66px;width:80px;height:32px">SIGNUP</div>
</footer>

<div class="abs bar">
  <span class="copyright">© Copyright 2019 Serena Condo</span>
  <ul class="menu">
    <li>HOME</li><li>ABOUT US</li><li>RESIDENTS</li><li>CONTACT US</li><li>ACCOUNT LOGIN</li>
  </ul>
</div>

</body>
</html>
```